Business card and Logo for a private personal training studio

We need a business card and logo for a private personal training studio.

The studios name is "Steady Your Path"
Main coloring to be a bright light blue. Looking for a crisp modern look

The front of the card is to have the

Studios name.
The Logo
Private Personal Training Studio
Mel Carver
0451 239 716

The back of the card is to have a lot of words relating to the services we offer. Please place the words vertically and horizontally using different fonts, different text sizes, different boldness and different colors to create a word picture.

Main words that need highlighting are

QVL, PILATES, BOXING, SPIN, STRENGTH, WEIGHT LOSS, BALANCE

Other words to add to the mix with less emphasis

Fitness, Conditioning, Lifestyle, Wellness, Health, Energy, Cardio, Goals, Muscle Tone, Vitality, Confidence, Attitude, Determination, Motivation, Dedication, Fun

Target Market(s)

Woman aged 30 to 60

Industry/Entity Type

Personal Trainer

Contact Information for Business Card

Steady Your Path
Mel Carver
0451 239 716

Colors
0493ce
33a6d7
85cae6

```html
<!DOCTYPE html>
<html lang="en">
<head>
<meta charset="utf-8">
<title>Steady Your Path – Business Card</title>
<link rel="stylesheet" href="https://fonts.googleapis.com/css2?family=Open+Sans:wght@400;600;700&display=swap">
<style>
  :root {
    --brand-blue: #0493ce;
    --brand-blue-mid: #33a6d7;
    --brand-blue-light: #85cae6;
    --ink: #111111;
    --muted-grey: #8c8c8c;
    --figure-grey: #e2e2e2;
    --card-white: #ffffff;
    --backdrop: #ececec;
  }
  * { margin: 0; padding: 0; box-sizing: border-box; }
  html, body { width: 1200px; height: 900px; overflow: hidden; }
  body { background: var(--backdrop); position: relative; font-family: "Open Sans", Arial, sans-serif; }

  .card { position: absolute; background: var(--card-white); overflow: hidden; box-shadow: 0 2px 10px rgba(0,0,0,0.12); }
  .card--front { left: 77px; top: 34px; width: 589px; height: 364px; }
  .card--back  { left: 389px; top: 506px; width: 565px; height: 352px; }

  .brand { position: absolute; display: flex; flex-direction: column; }
  .brand-row { display: flex; align-items: center; gap: 12px; }
  .brand-mark { width: 18px; height: 18px; border-radius: 50%; background: var(--brand-blue); flex: none; }
  .brand-name { font-family: "Open Sans", Arial, sans-serif; font-weight: 600; color: var(--brand-blue); white-space: nowrap; line-height: 1.1; }
  .brand-tagline { font-family: "Open Sans", Arial, sans-serif; font-weight: 400; color: var(--muted-grey); white-space: nowrap; text-transform: uppercase; letter-spacing: 1.6px; }

  .card--front .brand { left: 36px; top: 140px; }
  .card--front .brand-name { font-size: 34px; }
  .card--front .brand-tagline { font-size: 11px; margin-top: 6px; margin-left: 30px; }

  .contact-band { position: absolute; left: 0; top: 223px; width: 100%; height: 141px; background: var(--brand-blue); color: var(--card-white); }
  .contact-name { position: absolute; left: 31px; top: 40px; font-size: 21px; font-weight: 700; }
  .contact-phone { position: absolute; left: 31px; top: 81px; font-size: 15px; font-weight: 600; display: flex; align-items: center; gap: 6px; }
  .contact-phone svg { width: 12px; height: 12px; fill: var(--card-white); }

  .card--back .brand { left: 26px; top: 42px; }
  .card--back .brand-name { font-size: 30px; }
  .card--back .brand-tagline { font-size: 10.5px; margin-top: 5px; }

  .figure-fill { position: absolute; left: 384px; top: 68px; width: 181px; height: 272px; background: linear-gradient(180deg, var(--figure-grey), #f0f0f0); opacity: 0.7; }

  .services { position: absolute; left: 26px; top: 128px; color: var(--ink); }
  .services-main { font-size: 20px; font-weight: 700; line-height: 31px; white-space: nowrap; }
  .services-extra { margin-top: 27px; font-size: 15.5px; font-weight: 600; line-height: 25.7px; white-space: nowrap; }
</style>
</head>
<body>

  <section class="card card--front" aria-label="Card front">
    <div class="brand">
      <div class="brand-row">
        <span class="brand-mark" aria-hidden="true"></span>
        <span class="brand-name">Steady Your Path</span>
      </div>
      <span class="brand-tagline">Private Personal Training Studio</span>
    </div>
    <div class="contact-band">
      <div class="contact-name">Mel Carver</div>
      <div class="contact-phone">
        <svg viewBox="0 0 24 24" aria-hidden="true"><path d="M6.6 10.8c1.4 2.8 3.8 5.1 6.6 6.6l2.2-2.2c.3-.3.7-.4 1-.2 1.1.4 2.3.6 3.6.6.6 0 1 .4 1 1V20c0 .6-.4 1-1 1C10.6 21 3 13.4 3 4c0-.6.4-1 1-1h3.5c.6 0 1 .4 1 1 0 1.3.2 2.5.6 3.6.1.3 0 .7-.2 1l-2.3 2.2z"/></svg>
        <span>0451 239 716</span>
      </div>
    </div>
  </section>

  <section class="card card--back" aria-label="Card back">
    <div class="figure-fill" role="img" aria-label="Faint grey figures of a couple walking hand in hand"></div>
    <div class="brand">
      <span class="brand-name">Steady Your Path</span>
      <span class="brand-tagline">Private Personal Training Studio</span>
    </div>
    <div class="services">
      <p class="services-main">QVL | PILATES | BOXING | SPIN<br>STRENGTH | WEIGHT LOSS | BALANCE</p>
      <p class="services-extra">Fitness | Conditioning | Lifestyle | Wellness<br>Health | Energy | Cardio | Goals | Muscle Tone<br>Vitality | Confidence | Attitude | Determination<br>Motivation | Dedication | Fun</p>
    </div>
  </section>

</body>
</html>
```